Business Card - Professional Minimalist - Double sided

We appreciate minimalist logo/web/collateral designs that allow design to tell a story. We want to relay a professional image/approach but throwing in a splash of modern when we’re able so long as it’s not distracting. Think 75% classic corporate, 25% modern. Open to black or white design, not sure which might look the best.

Target Market(s)

Senior executives or related government affairs contacts within the agriculture, energy, and defense industries (i.e., potential clients) but located outside of Washington, DC. Most potential clients based in DC with be familiar with both of us and our shared history.

Industry/Entity Type

Consulting

Contact Information for Business Card

Name: Daniel R. Whitlock
Title: Co-Founder & Partner
Address: 418 Bramblewood Ave. SE | Suite 2716 | Washington, D.C. 20019
Phone: (202) 555-0187
Email: Daniel@HollerbyWhitlock.com

Font styles to use
Serif

Colors

Designer to choose only greyscale colors for use in the design.

Requirements
Must have
• Name: Daniel R. Whitlock
Phone: (202) 555-0187

```html
<!DOCTYPE html>
<html lang="en">
<head>
<meta charset="utf-8">
<title>Hollerby Whitlock Group – Business Card</title>
<link href="https://fonts.googleapis.com/css2?family=Tinos&family=Arimo:wght@400;700&display=swap" rel="stylesheet">
<style>
  :root {
    --backdrop: #d9d9d7;
    --card-dark: #1f1d1e;
    --card-light: #ffffff;
    --ink-dark: #3b3b3b;
    --ink-mid: #8a8a8a;
    --ink-light: #b9b9b9;
    --rule: #9a9a9a;
    --mark-soft: #a9a9a9;
  }
  * { box-sizing: border-box; margin: 0; padding: 0; }
  html, body { width: 1200px; height: 900px; overflow: hidden; }
  body {
    background: var(--backdrop);
    display: flex;
    flex-direction: column;
    align-items: center;
    justify-content: center;
    gap: 36px;
  }
  .card {
    position: relative;
    width: 700px;
    height: 400px;
    overflow: hidden;
    box-shadow: 0 6px 18px rgba(0,0,0,0.18);
  }
  .card--front { background: var(--card-dark); }
  .card--back { background: var(--card-light); }

  .wordmark {
    position: absolute;
    display: flex;
    align-items: center;
    gap: 12px;
    font-family: "Tinos", "Times New Roman", serif;
    text-transform: uppercase;
    letter-spacing: 0.04em;
    white-space: nowrap;
  }
  .wordmark__square { width: 22px; height: 22px; }
  .wordmark__name { display: flex; flex-direction: column; }
  .wordmark__title { line-height: 1; }
  .wordmark__rule { height: 1px; background: var(--rule); margin-top: 6px; }

  .card--front .wordmark { left: 96px; top: 236px; color: var(--ink-light); }
  .card--front .wordmark__title { font-size: 30px; }
  .card--front .wordmark__square { background: var(--ink-light); width: 28px; height: 28px; }

  .card--back .wordmark { left: 54px; top: 50px; color: var(--ink-dark); }
  .card--back .wordmark__title { font-size: 27px; }
  .card--back .wordmark__square { background: var(--ink-dark); width: 26px; height: 26px; }

  .feature-shape {
    position: absolute;
    border-radius: 50%;
  }
  .card--front .feature-shape { right: -60px; top: -40px; width: 250px; height: 250px; background: #4a4a4a; }
  .card--back .feature-shape { right: -40px; top: 110px; width: 250px; height: 250px; background: var(--mark-soft); }

  .contact {
    position: absolute;
    left: 54px;
    top: 132px;
    font-family: "Arimo", Arial, sans-serif;
    color: var(--ink-dark);
    font-size: 17px;
    line-height: 1.25;
  }
  .contact__name { font-weight: 700; font-size: 21px; }
  .contact__role { margin-bottom: 18px; }
  .contact__address { margin-bottom: 18px; }
</style>
</head>
<body>
  <section class="card card--front" aria-label="Card front">
    <div class="feature-shape"></div>
    <div class="wordmark">
      <span class="wordmark__square"></span>
      <span class="wordmark__name">
        <span class="wordmark__title">Hollerby Whitlock Group</span>
        <span class="wordmark__rule"></span>
      </span>
    </div>
  </section>

  <section class="card card--back" aria-label="Card back">
    <div class="feature-shape"></div>
    <div class="wordmark">
      <span class="wordmark__square"></span>
      <span class="wordmark__name">
        <span class="wordmark__title">Hollerby Whitlock Group</span>
        <span class="wordmark__rule"></span>
      </span>
    </div>
    <div class="contact">
      <p class="contact__name">Daniel R. Whitlock</p>
      <p class="contact__role">Co-Founder &amp; Partner</p>
      <p class="contact__address">418 Bramblewood Ave. SE<br>Suite 2716<br>Washington, D.C. 20019</p>
      <p>P: (202) 555-0187</p>
      <p>E: Daniel@HollerbyWhitlock.com</p>
    </div>
  </section>
</body>
</html>
```